Business card logo/design needed

I need a new and fresh business card to get my name out there.
I have made plenty before and have a logo but I dont think it is sending the right message across.
I am a personal trainer running a small online business designed to cut the cost of training by taking it online, allowing you to purchase training over the net, through the help of Skype and video uploads.
You can personalized programs hand written for you or more general programs aimed at your goals.
Our goal is to get everyone to look like and behave like an athlete because there is no point in being in shape if you cant do anything with that body.
I also have a strong background in sports, having played low level college basketball in america and worked as a strength and conditioning coach. I dont like running or slow cardio, I am more focused on weights and functional training for aerobic fitness.
I am young for what I do, but I have lot of knowledge and I need something that says that I am not your standard drill sergeant trainer but someone who will truly help you reach your goals.
My curent logo text is "the climb to the top" but I am not set on that.

Industry/Entity Type

Personal Trainer

Contact Information for Business Card

Desmond Quilby
Summit Forge Motion
Personal trainer
Strength and conditioning coach
0481 552 709
www.summitforgemotion.example

```html
<!DOCTYPE html>
<html lang="en">
<head>
<meta charset="utf-8">
<title>Summit Forge Motion – Business Card</title>
<link href="https://fonts.googleapis.com/css2?family=Carlito:ital,wght@0,400;0,700;1,400&display=swap" rel="stylesheet">
<style>
  :root {
    --navy: #1b2a5c;
    --frame: #17244f;
    --grey: #7b7b7b;
    --grey-blue: #6a6e80;
    --paper: #ffffff;
    --sketch-light: #e9e9e9;
    --sketch-dark: #9a9a9a;
  }
  html, body {
    margin: 0;
    padding: 0;
    overflow: hidden;
    background: var(--paper);
  }
  .card {
    position: relative;
    width: 1200px;
    height: 693px;
    box-sizing: border-box;
    background: var(--paper);
    border: 9px solid var(--frame);
    border-radius: 22px;
    overflow: hidden;
    font-family: "Carlito", "Calibri", sans-serif;
  }
  .card__illustration {
    position: absolute;
    left: 400px;
    top: 70px;
    width: 780px;
    height: 605px;
    border-radius: 48% 40% 30% 46%;
    background: radial-gradient(ellipse at 45% 55%, var(--sketch-dark) 0%, #bdbdbd 40%, var(--sketch-light) 75%, rgba(255,255,255,0) 100%);
  }
  .brand {
    position: absolute;
    left: 14px;
    top: 8px;
    margin: 0;
    font-size: 70px;
    font-weight: 400;
    line-height: 1;
    color: var(--navy);
  }
  .role {
    position: absolute;
    left: 106px;
    top: 84px;
    margin: 0;
    font-size: 42px;
    line-height: 1;
    color: var(--navy);
  }
  .motto {
    position: absolute;
    left: 14px;
    top: 148px;
    margin: 0;
    font-size: 24px;
    font-style: italic;
    line-height: 1;
    color: var(--navy);
  }
  .contact {
    position: absolute;
    left: 14px;
    top: 368px;
    margin: 0;
    color: var(--grey);
    line-height: 1;
  }
  .contact__name {
    display: block;
    font-size: 82px;
    margin-bottom: 10px;
  }
  .contact__title {
    display: block;
    font-size: 56px;
    font-weight: 700;
    margin-bottom: 14px;
  }
  .contact__phone,
  .contact__web {
    display: block;
    font-size: 54px;
    color: var(--grey-blue);
    letter-spacing: 1px;
  }
  .contact__phone { margin-bottom: 14px; }
</style>
</head>
<body>
  <div class="card">
    <div class="card__illustration" role="img" aria-label="Pencil sketch of a hand gripping a kettlebell handle"></div>

    <h1 class="brand">Summit Forge Motion</h1>
    <p class="role">Strength &amp; conditioning coach</p>
    <p class="motto">"Wake up with determination, go to bed with satisfaction."</p>

    <address class="contact">
      <span class="contact__name">Desmond Quilby</span>
      <span class="contact__title">Personal Trainer</span>
      <span class="contact__phone">0481 552 709</span>
      <span class="contact__web">www.summitforgemotion.example</span>
    </address>
  </div>
</body>
</html>
```